new branding The Velvet Sip House

The Velvet Sip House is a Belgian brand of ready to serve mocktails. We're looking for a rebranding of the labels on our bottles (8 different flavours)
Our mocktails are low in sugar, 100% natural and completely alcohol-free. They are also 'ready to serve': gently shake the bottle, serve with ice cubes, finish and your mocktail is ready in no time!
Besides being the ideal aperitif, you can also serve them during brunch or dinner. Thanks to the different flavors, you can pair each mocktail with a dish.
Please visit our website to see the current look&feel: the velvetsiphouse.com - https://thevelvetsiphouse.glimmerfold.com/

Target Market(s)

people looking for a premium alcoholfree alternative - premium market

Industry/Entity Type

Mocktails (our mocktails have unique flavors, it's not the non-alcoholic version of a cocktail)

Colors

Designer to choose colors to be used in the design.

Requirements
Must have
• Our brand should be more visible, more recognizable, bolder, without losing the premium and refined character. Base colors should be white, black and silver. The brand should be put more foward. Keep number concept (every mocktail has its number) Put the ingredients/flavours/combinations a bit more forward. make the brand more confident and mature. The eight bottles should become a family. PREMIUM EXPRESSION
Nice to have
• We want to work with a white label. Ideas for the shape of the label Some ideas for the label: Play with shapes, cut outs, texture and number of labels. We like the frosted look and the combination of print & label . Working with 2 labels gives it more dynamic, not one big block Clean label. Working with a cut out shape, can be the logo or the numbers ? Working with 2 labels makes it easier to create an importance of messages. Working with an organic shape makes it unique and give a natural touch Working with a cut out can give a color pop on the white label The label can have parts coming out of the square shape
Should not have
• No crazy stuff, finishes etc should be feasible/realistic

```html
<!DOCTYPE html>
<html lang="en">
<head>
<meta charset="utf-8">
<title>The Velvet Sip House — Premium Expression Label</title>
<link rel="stylesheet" href="https://fonts.googleapis.com/css2?family=Oswald:wght@200&family=Ubuntu:wght@500&display=swap">
<style>
  :root {
    --page: #ffffff;
    --label-black: #141414;
    --label-graphite: #2e2e30;
    --label-silver: #b9bbbf;
    --label-white: #f6f6f7;
    --silver-band: #9a9ca1;
    --ink-light: #ffffff;
  }
  * { margin: 0; padding: 0; box-sizing: border-box; }
  html, body {
    width: 1200px;
    height: 1200px;
    overflow: hidden;
    background: var(--page);
  }
  .canvas {
    position: relative;
    width: 1200px;
    height: 1200px;
  }
  .label {
    position: absolute;
    left: 254px;
    top: 81px;
    width: 692px;
    height: 1038px;
    overflow: hidden;
    background: var(--label-white);
  }
  .label-field {
    position: absolute;
    inset: 0;
    width: 100%;
    height: 100%;
  }
  .label-text {
    position: absolute;
    left: 0;
    width: 100%;
    text-align: center;
    color: var(--ink-light);
    white-space: nowrap;
  }
  .brand-name {
    font-family: "Oswald", sans-serif;
    font-weight: 200;
    line-height: 1;
  }
  .brand-name--first {
    top: 102px;
    font-size: 94px;
    letter-spacing: 0.01em;
  }
  .brand-name--second {
    top: 202px;
    font-size: 94px;
    letter-spacing: 0.12em;
    padding-left: 0.12em;
  }
  .range-title {
    font-family: "Ubuntu", sans-serif;
    font-weight: 500;
    font-size: 33px;
    letter-spacing: 0.2em;
    padding-left: 0.2em;
    line-height: 1;
  }
  .range-title--first { top: 439px; }
  .range-title--second { top: 487px; }
  .divider {
    position: absolute;
    left: 99px;
    top: 591px;
    width: 494px;
    height: 50px;
  }
  .divider-number {
    font-family: "Ubuntu", sans-serif;
    font-weight: 500;
    font-size: 15px;
    letter-spacing: 0.05em;
    fill: var(--ink-light);
  }
  .product-detail {
    font-family: "Ubuntu", sans-serif;
    font-weight: 500;
    font-size: 34px;
    line-height: 1;
  }
  .product-detail--flavour { top: 729px; }
  .product-detail--type { top: 781px; }
  .product-detail--volume { top: 885px; }
</style>
</head>
<body>
<main class="canvas">
  <section class="label" aria-label="The Velvet Sip House bottle label">
    <svg class="label-field" viewBox="0 0 555 830" preserveAspectRatio="none" aria-hidden="true">
      <defs>
        <radialGradient id="field-glow" cx="0.5" cy="0.48" r="0.62">
          <stop offset="0" stop-color="#141414"/>
          <stop offset="0.45" stop-color="#222224"/>
          <stop offset="0.75" stop-color="#7d7f84"/>
          <stop offset="1" stop-color="#f6f6f7"/>
        </radialGradient>
        <filter id="soft" x="-20%" y="-20%" width="140%" height="140%">
          <feGaussianBlur stdDeviation="9"/>
        </filter>
      </defs>
      <rect width="555" height="830" fill="url(#field-glow)"/>
      <g filter="url(#soft)">
        <polygon points="0,760 555,205 555,250 0,805" fill="#e4e5e8" opacity="0.55"/>
        <polygon points="0,735 555,180 555,205 0,760" fill="#9a9ca1" opacity="0.8"/>
        <polygon points="150,830 555,425 555,470 195,830" fill="#e4e5e8" opacity="0.5"/>
        <polygon points="190,830 555,465 555,490 215,830" fill="#9a9ca1" opacity="0.75"/>
        <polygon points="470,830 555,745 555,830" fill="#f6f6f7"/>
        <polygon points="455,830 555,730 555,752 478,830" fill="#9a9ca1" opacity="0.8"/>
      </g>
    </svg>

    <h1 class="label-text brand-name brand-name--first">THE VELVET</h1>
    <p class="label-text brand-name brand-name--second">SIP HOUSE</p>

    <p class="label-text range-title range-title--first">PREMIUM</p>
    <p class="label-text range-title range-title--second">EXPRESSION</p>

    <svg class="divider" viewBox="0 0 494 50" aria-label="Mocktail number 01" role="img">
      <path d="M0 25 Q110 23.5 222 24 L222 26 Q110 26.5 0 25 Z" fill="#ffffff"/>
      <path d="M272 24 Q384 23.5 494 25 Q384 26.5 272 26 Z" fill="#ffffff"/>
      <circle cx="247" cy="25" r="20" fill="none" stroke="#ffffff" stroke-width="2.5"/>
      <text class="divider-number" x="247" y="30.5" text-anchor="middle">01</text>
    </svg>

    <p class="label-text product-detail product-detail--flavour">FLAVOUR</p>
    <p class="label-text product-detail product-detail--type">NON-ALCOHOLIC</p>
    <p class="label-text product-detail product-detail--volume">16 FL OZ</p>
  </section>
</main>
</body>
</html>
```